A Freight forwarding (transportation/shipping) company requires stationary design

We need The following:
1. Letterhead
2. Letter Envelope
3. A4 Paper Envelope
4. A4 Paper Folder (One that is 2xA4 foldable size which we can open in half and we can put a paper in between)
5. A5 Paper (To be used for notes taking)

a design for a freight forwarding company named VORELTA DUNIMOR INTERNATIONAL TRANSPORTATION CO . Business Card is already designed and should follow it, the files attached help guide you in type of docs required + Logos (We are active in Sea Transportation, Truck transportation, and Air Transportation, (printed design is required with all open source files for editing - lamination accepted)

The said company is agent and sales representative of 2 other Shipping companies (whose logos, name, and website should also be mentioned on Envelopes and Folder) - Bold Wave and TQN Shipping, logos attached.

Bold Wave Shipping LLC
Dubai, United Arab Emirates
www.bwsmarine-example.com

TQN Shipping Line Ltd
London, United Kingdom
www.tqnlinex-example.com

Address is "No.7, 2nd Soltani-e-Norvand, Tehran, IR
Tel number is +98 21 55302914
Fax number is +98 21 55306631
E-Mail address is info@voreltadunimor-example.com
Website is www.voreltadunimor-example.com

```html
<!DOCTYPE html>
<html lang="en">
<head>
<meta charset="utf-8">
<title>Vorelta Dunimor – Envelope Front and Back</title>
<link href="https://fonts.googleapis.com/css2?family=Fira+Sans:wght@400;500&family=Oswald:wght@600&display=swap" rel="stylesheet">
<style>
  :root {
    --backdrop: #243659;
    --flap: #344a74;
    --paper: #ffffff;
    --watermark: #f1f2f3;
    --brand-ink: #2d2a6e;
    --brand-blue: #1f6fae;
    --partner-ink: #1c4460;
    --rule-grey: #dcdde0;
    --ring-grey: #a9aaad;
  }
  html, body { margin: 0; padding: 0; }
  body {
    width: 1200px; height: 900px; overflow: hidden;
    background: var(--backdrop);
    position: relative;
    font-family: "Fira Sans", sans-serif;
  }
  .envelope {
    position: absolute; top: 124px; width: 402px; height: 652px;
    filter: drop-shadow(0 6px 14px rgba(0,0,0,.25));
  }
  .envelope--front { left: 134px; }
  .envelope--back { left: 610px; }
  .envelope__flap { position: absolute; top: 0; left: 0; width: 402px; height: 84px; display: block; }
  .envelope__body {
    position: absolute; top: 83px; left: 0; width: 402px; height: 569px;
    background: var(--paper);
  }
  .envelope__edge {
    position: absolute; left: 0; bottom: 0; width: 100%; height: 4px;
    background: var(--rule-grey);
  }
  .envelope__edge::after {
    content: ""; position: absolute; left: 138px; width: 142px; height: 100%;
    background: var(--brand-blue);
  }
  .watermark-area {
    position: absolute;
    background: radial-gradient(ellipse at center, var(--watermark) 0%, var(--watermark) 55%, rgba(241,242,243,0) 72%);
  }
  .watermark-area--front { left: 50px; top: 17px; width: 304px; height: 352px; }
  .watermark-area--back { left: 38px; top: 49px; width: 328px; height: 384px; }
  .brand-block {
    position: absolute; left: 60px; top: 410px;
    display: flex; align-items: center; gap: 12px;
  }
  .brand-block__ring {
    width: 104px; height: 104px; border-radius: 50%;
    border: 2px solid var(--ring-grey); box-sizing: border-box; flex: none;
  }
  .brand-block__name {
    margin: 0; color: var(--brand-ink); font-weight: 500;
    font-size: 22px; line-height: 28.5px; text-align: center;
  }
  .contact-line {
    position: absolute; left: 0; right: 0; bottom: 10px;
    display: flex; justify-content: center; gap: 4px; align-items: center;
    font-size: 5.2px; color: var(--partner-ink); white-space: nowrap;
  }
  .contact-line__dot {
    width: 4px; height: 4px; border-radius: 50%; background: var(--brand-blue); display: inline-block;
  }
  .partner {
    position: absolute; bottom: 14px; display: flex; align-items: center; gap: 6px;
    color: var(--partner-ink);
  }
  .partner--left { left: 14px; }
  .partner--right { right: 12px; }
  .partner__mark { width: 30px; height: 30px; border-radius: 50%; background: var(--partner-ink); flex: none; }
  .partner__mark--outline { background: none; border: 1.5px solid var(--partner-ink); box-sizing: border-box; width: 26px; height: 26px; }
  .partner__text { text-align: center; line-height: 1.15; }
  .partner__name { font-family: "Oswald", sans-serif; font-weight: 600; font-size: 7.5px; letter-spacing: .8px; text-transform: uppercase; }
  .partner__detail { font-size: 5.4px; }
</style>
</head>
<body>

<section class="envelope envelope--front" aria-label="Envelope front">
  <svg class="envelope__flap" viewBox="0 0 402 84" aria-hidden="true">
    <path d="M0 84 L12 20 Q16 0 36 0 L366 0 Q386 0 390 20 L402 84 Z" fill="var(--flap)"/>
  </svg>
  <div class="envelope__body">
    <div class="watermark-area watermark-area--front" role="img" aria-label="Large faint company emblem watermark"></div>
    <div class="brand-block">
      <div class="brand-block__ring"></div>
      <p class="brand-block__name">Vorelta Dunimor<br>International<br>Transport.Co L.Lc</p>
    </div>
    <div class="contact-line">
      <span class="contact-line__dot"></span><span>No.7, 2nd Soltani-e-Norvand, Tehran, IR</span>
      <span class="contact-line__dot"></span><span>+98 21 55302914</span>
      <span class="contact-line__dot"></span><span>+98 21 55306631</span>
      <span class="contact-line__dot"></span><span>info@voreltadunimor-example.com</span>
      <span class="contact-line__dot"></span><span>www.voreltadunimor-example.com</span>
    </div>
    <div class="envelope__edge"></div>
  </div>
</section>

<section class="envelope envelope--back" aria-label="Envelope back">
  <svg class="envelope__flap" viewBox="0 0 402 84" aria-hidden="true">
    <path d="M0 84 L12 20 Q16 0 36 0 L366 0 Q386 0 390 20 L402 84 Z" fill="var(--flap)"/>
  </svg>
  <div class="envelope__body">
    <div class="watermark-area watermark-area--back" role="img" aria-label="Large faint company emblem watermark"></div>
    <div class="partner partner--left">
      <div class="partner__mark"></div>
      <div class="partner__text">
        <div class="partner__name">Bold Wave<br>Shipping LLC</div>
        <div class="partner__detail">Dubai, UAE<br>www.bwsmarine-example.com</div>
      </div>
    </div>
    <div class="partner partner--right">
      <div class="partner__mark partner__mark--outline"></div>
      <div class="partner__text">
        <div class="partner__name">TQN</div>
        <div class="partner__detail">Shipping Line Ltd<br>London, UK<br>www.tqnlinex-example.com</div>
      </div>
    </div>
    <div class="envelope__edge"></div>
  </div>
</section>

</body>
</html>
```